Business Card design
Cordavera Ruvek Martial Arts Training Center
I need single sided standard sized Business Card [3.5" x 2"]
Font in logo is CGF Locust Resistance. This font does not need to be used.
Modern
Cordavera Ruvek or Cordavera Ruvek Martial Arts Training Center
Martial Arts Discipline | Athletic Excellence
2671 Bramble Rd
Kalamazoo, MI
info@cordaverix.example
www.cordaverix.example
facebook.com/cordaverix
optional items for the business card:
Pelnor Grappling League
Todd Weslin Jiu Jitsu
Orvane Kickboxing Union
Mixed Martial Arts
Fitness
Can put the logo on one side and the information on the second side if you would like to submit that type of design.
Cordavera Ruvek illustrator file
Cordavera Ruvek eps file

```html
<!DOCTYPE html>
<html lang="en">
<head>
<meta charset="utf-8">
<title>Cordavera Ruvek Stationery</title>
<link href="https://fonts.googleapis.com/css2?family=Roboto:wght@400;700&display=swap" rel="stylesheet">
<style>
  :root {
    --red: #ef4136;
    --red-dark: #d8322a;
    --grey: #8e8e8e;
    --grey-light: #c9c9c9;
    --paper: #ffffff;
    --backdrop: #ececec;
    --ink: #3a3a3a;
  }
  * { margin: 0; padding: 0; box-sizing: border-box; }
  html, body { width: 1200px; height: 643px; overflow: hidden; }
  body { background: var(--backdrop); font-family: "Roboto", Arial, sans-serif; color: var(--ink); }
  .canvas { position: relative; width: 1200px; height: 643px; }

  .piece { position: absolute; background: var(--paper); box-shadow: 0 1px 3px rgba(0,0,0,.18); overflow: hidden; }

  .wordmark { font-weight: 700; letter-spacing: .04em; text-transform: uppercase; color: var(--red); white-space: nowrap; }

  .contact { font-size: 4.2px; line-height: 6px; color: var(--ink); }

  /* business cards */
  .card { top: 29px; width: 156px; height: 91px; border-radius: 3px; }
  .card--red { background: var(--red); }
  .card--grey { background: linear-gradient(135deg, #a6a6a6, #7d7d7d); }
  .card--red .wordmark, .card--grey .wordmark {
    color: #fff; font-size: 11px; position: absolute; left: 0; right: 0; top: 39px; text-align: center;
  }
  .card--info .wordmark { position: absolute; left: 9px; top: 11px; font-size: 8px; }
  .card--info .contact { position: absolute; left: 74px; top: 32px; }
  .card__swoosh { position: absolute; inset: 0; }

  /* letterheads */
  .letterhead { top: 144px; width: 362px; height: 485px; }
  .letterhead .wordmark { position: absolute; left: 18px; top: 18px; font-size: 10px; }
  .letterhead .contact { position: absolute; left: 18px; bottom: 20px; }
  .letterhead__corner { position: absolute; right: 0; bottom: 0; }

  /* envelopes */
  .envelope { left: 802px; width: 378px; }
  .envelope--front { top: 144px; height: 221px; }
  .envelope__window { position: absolute; right: 22px; top: 18px; width: 118px; height: 18px; border-radius: 3px; background: #dcdcdc; }
  .envelope--front .contact { position: absolute; left: 18px; top: 160px; }
  .envelope__rule { position: absolute; left: 0; right: 0; bottom: 16px; height: 3px; background: var(--red); }
  .envelope__rule--grey { bottom: 11px; height: 3px; background: var(--grey-light); }

  .envelope--back { top: 384px; height: 245px; }
  .envelope__band { position: absolute; left: 0; right: 0; top: 24px; height: 48px; background: var(--red); display: flex; align-items: center; justify-content: center; }
  .envelope__band .wordmark { color: #fff; font-size: 12px; }
</style>
</head>
<body>
<main class="canvas">

  <!-- business cards -->
  <section class="piece card card--red" style="left:24px"><span class="wordmark">Cordavera Ruvek</span></section>
  <section class="piece card card--grey" style="left:192px"><span class="wordmark">Cordavera Ruvek</span></section>

  <section class="piece card card--info" style="left:360px">
    <svg class="card__swoosh" viewBox="0 0 156 91" aria-hidden="true"><path d="M156 0 H120 C135 25 132 60 100 91 H156 Z" fill="var(--red)"/><path d="M114 0 C128 25 124 60 92 91 H98 C130 60 133 25 118 0 Z" fill="var(--grey-light)"/></svg>
    <span class="wordmark">Cordavera Ruvek</span>
    <p class="contact" style="left:9px">2671 Bramble Rd<br>Kalamazoo, MI<br>info@cordaverix.example<br>www.cordaverix.example</p>
  </section>

  <section class="piece card card--info" style="left:532px">
    <svg class="card__swoosh" viewBox="0 0 156 91" aria-hidden="true"><path d="M0 91 V70 C50 80 110 78 156 60 V91 Z" fill="var(--red)"/></svg>
    <span class="wordmark">Cordavera Ruvek</span>
    <p class="contact" style="left:9px;top:30px">2671 Bramble Rd<br>Kalamazoo, MI<br>info@cordaverix.example<br>www.cordaverix.example</p>
  </section>

  <section class="piece card card--info" style="left:700px">
    <svg class="card__swoosh" viewBox="0 0 156 91" aria-hidden="true"><path d="M0 91 V76 C60 70 110 84 156 66 V91 Z" fill="var(--red)"/><path d="M0 72 C60 66 110 80 156 62 V65 C110 83 60 69 0 75 Z" fill="var(--grey-light)"/></svg>
    <span class="wordmark">Cordavera Ruvek</span>
    <p class="contact" style="left:9px;top:30px">2671 Bramble Rd<br>Kalamazoo, MI<br>info@cordaverix.example<br>www.cordaverix.example</p>
  </section>

  <section class="piece card card--info" style="left:868px">
    <svg class="card__swoosh" viewBox="0 0 156 91" aria-hidden="true"><path d="M156 0 H126 C140 30 136 62 110 91 H156 Z" fill="var(--red)"/></svg>
    <span class="wordmark">Cordavera Ruvek</span>
    <p class="contact" style="left:9px;top:30px">2671 Bramble Rd<br>Kalamazoo, MI<br>info@cordaverix.example<br>www.cordaverix.example</p>
  </section>

  <section class="piece card card--info" style="left:1036px">
    <svg class="card__swoosh" viewBox="0 0 156 91" aria-hidden="true"><path d="M0 91 V78 C60 72 100 86 156 70 V91 Z" fill="var(--red)"/><path d="M156 0 H136 C146 20 144 40 132 58 H156 Z" fill="var(--red)"/></svg>
    <span class="wordmark">Cordavera Ruvek</span>
    <p class="contact" style="left:9px;top:30px">2671 Bramble Rd<br>Kalamazoo, MI<br>info@cordaverix.example<br>www.cordaverix.example</p>
  </section>

  <!-- letterheads -->
  <section class="piece letterhead" style="left:34px">
    <span class="wordmark">Cordavera Ruvek</span>
    <p class="contact">2671 Bramble Rd<br>Kalamazoo, MI<br>info@cordaverix.example<br>www.cordaverix.example</p>
    <svg class="letterhead__corner" width="120" height="16" viewBox="0 0 120 16" aria-hidden="true"><path d="M20 8 H120 V16 H12 Z" fill="var(--red)"/><path d="M40 4 H120 V8 H36 Z" fill="var(--grey-light)"/></svg>
  </section>

  <section class="piece letterhead" style="left:420px">
    <span class="wordmark">Cordavera Ruvek</span>
    <p class="contact">2671 Bramble Rd<br>Kalamazoo, MI<br>info@cordaverix.example<br>www.cordaverix.example</p>
    <svg class="letterhead__corner" width="120" height="16" viewBox="0 0 120 16" aria-hidden="true"><path d="M20 8 H120 V16 H12 Z" fill="var(--red)"/><path d="M40 4 H120 V8 H36 Z" fill="var(--grey-light)"/></svg>
  </section>

  <!-- envelopes -->
  <section class="piece envelope envelope--front">
    <div class="envelope__window"></div>
    <p class="contact">2671 Bramble Rd<br>Kalamazoo, MI<br>info@cordaverix.example<br>www.cordaverix.example</p>
    <div class="envelope__rule"></div>
    <div class="envelope__rule envelope__rule--grey"></div>
  </section>

  <section class="piece envelope envelope--back">
    <div class="envelope__band"><span class="wordmark">Cordavera Ruvek</span></div>
  </section>

</main>
</body>
</html>
```